We need a brochure design for the Institute For Civic Pathways a community organizing training and a capacity building program. ICP currently has 2 programs, an apprenticeship program and a training course. We expect to add additional programs. The program is not aimed at young people, however the majority of the participants are under 30. The brochure is aimed at funders (foundations etc.) and potential participating organizations, rather than the actual apprenticeship or course participants. The purpose of the brochure is to demonstrate the effectiveness of the program. The design should communicate **vibrancy, success, growth, **a grassroots approach, learning, and personal development. The brochure should have space for data e.g. "xyz% of participants go on to do ABC", room for "where are they now" testimonials, 4-7 photos and a program overview.

Shape and Size:
- We are flexible about shape and size but we are imagining a tri-fold document
Size:
-Approximately 11.5 or 12 x 6 inches.
-Ideally the document would fold out to 18 x 12 if we choose the fold out model can you include some sort of notch out or design element to indicate that the document opens.

The attachment is only to show the fold layout we want (as a folding dummy). We don't want to reproduce this design look, only the way the brochure unfolds not any of the design elements or content. The layout we want is: trifold brochure to poster with 12 total panels.

Color:

Attached is our logo so you have an idea of the colors etc. we are looking for.

This is an old website, we don't want to use this color scheme etc., but it gives you a feel for the program: http://brovalentrust.org/icpvel/

Target Market(s)

The brochure is aimed at funders (foundations etc.) and potential participating organizations, rather than the actual apprenticeship or course participants. Adults 30+.
While the readers will be interested in the youthful energy of the program participants, the brochure isn't aimed at young people.

Industry/Entity Type

Training

Requirements
Must have
• Ideally the document would fold out to 11 x 17 if we choose the fold out model can you include some sort of notch out or design element to indicate that the document opens.

The attachment is only to show the fold layout we want (as a folding dummy). We don't want to reproduce this design look, only the way the brochure unfolds not any of the design elements or content. The layout we want is: trifold brochure to poster with 12 total panels. The outside should have information about the program and the inside can have a graphic(s) and photos of past participants along with short testimonials.

```html
<!DOCTYPE html>
<html lang="en">
<head>
<meta charset="utf-8">
<title>Institute For Civic Pathways — Service Excellence Brochure</title>
<link rel="stylesheet" href="https://fonts.googleapis.com/css2?family=Source+Sans+3:wght@300;400;600;700&display=swap">
<style>
  :root{
    --navy:#1b4f7a;
    --navy-deep:#0c3a5c;
    --blue:#1e5b86;
    --blue-dark:#0f3f66;
    --red:#e8262b;
    --red-dark:#a3141a;
    --grey-panel:#d1d2d4;
    --ink:#1a1a1a;
    --white:#ffffff;
    --row-alt:#e6e6e6;
    --chart-line:#29a8e0;
  }
  *{margin:0;padding:0;box-sizing:border-box}
  html,body{width:1200px;height:1000px;overflow:hidden;background:var(--white)}
  body{position:relative;font-family:"Source Sans 3",Arial,sans-serif;color:var(--ink)}
  .abs{position:absolute}

  .shapes{position:absolute;left:0;top:0}

  .photo{position:absolute}
  .photo--workshop{left:95px;top:178px;width:677px;height:277px;
    background:linear-gradient(135deg,#3f4a2c 0%,#6b5a47 35%,#8a6c5c 55%,#4d4a3a 80%,#2f3526 100%)}
  .photo--group{left:250px;top:518px;width:254px;height:140px;border:2px solid #cfe0ec;
    background:linear-gradient(160deg,#8c8a63 0%,#6e6a52 45%,#5b5546 100%)}

  .tagline{left:80px;top:375px;width:250px;height:63px;
    background:linear-gradient(90deg,var(--red-dark),var(--red));
    color:var(--white);font-size:15.5px;line-height:16px;padding:10px 0 0 27px;letter-spacing:.3px}

  .title{left:215px;top:104px;font-size:57px;font-weight:400;color:var(--navy);letter-spacing:-.3px;line-height:1}

  .partner{left:832px;top:118px;width:300px}
  .partner h2{font-size:28px;font-weight:400;color:var(--red);line-height:1}
  .partner h3{font-size:17px;font-weight:400;color:var(--ink);margin-top:8px;line-height:1.1}
  .partner p{font-size:12px;line-height:15px;margin-top:5px}
  .partner p+p{margin-top:15px}

  .results{left:760px;top:388px;width:432px;height:307px;
    background:linear-gradient(100deg,var(--navy-deep) 0%,#175c89 55%,#2a7aab 100%)}
  .results h2{position:absolute;left:72px;top:20px;font-size:26px;font-weight:400;color:var(--white);line-height:1}
  .results p{position:absolute;left:72px;top:54px;width:340px;font-size:12px;line-height:15.3px;color:var(--white)}

  .data-table{position:absolute;left:70px;top:179px;width:333px;border-collapse:collapse;font-size:7.5px;text-align:center}
  .data-table th{background:var(--navy-deep);color:var(--white);font-weight:700;height:13px;border:1px solid #9fb3c4;letter-spacing:.3px}
  .data-table td{height:12.8px;border:1px solid #c9c9c9;background:var(--white);color:var(--ink)}
  .data-table tr:nth-child(odd) td{background:var(--row-alt)}

  .contact{left:240px;top:508px;width:495px;height:160px;
    background:linear-gradient(100deg,var(--navy-deep) 0%,#1c628f 60%,#2a7aab 100%)}
  .contact h2{position:absolute;left:278px;top:17px;font-size:24px;font-weight:400;color:var(--white);line-height:1}
  .contact .rule{position:absolute;left:278px;top:47px;width:197px;height:1px;background:#9cc3dc}
  .contact p{position:absolute;left:278px;top:54px;width:200px;font-size:12.5px;line-height:15.5px;color:var(--white)}

  .academy-bg{left:400px;top:668px;width:400px;height:297px;background:var(--grey-panel)}

  .program{top:728px;width:342px}
  .program h2{font-size:28px;font-weight:300;color:var(--navy);line-height:1;white-space:nowrap}
  .program p{font-size:11.6px;line-height:15.3px;margin-top:14px;text-align:justify}
  .program--apprentice{left:28px}
  .program--academy{left:430px}

  .chart{left:830px;top:715px}
  .chart-label{font-size:11px;fill:var(--chart-line);font-family:"Source Sans 3",Arial,sans-serif}
  .chart-total{font-size:32px;fill:var(--navy);font-family:"Source Sans 3",Arial,sans-serif}
  .chart-total tspan{font-size:17px}
  .legend-label{font-size:5.5px;fill:var(--navy);font-family:"Source Sans 3",Arial,sans-serif}
</style>
</head>
<body>

<svg class="shapes" width="1200" height="1000" viewBox="0 0 1200 1000" aria-hidden="true">
  <defs>
    <linearGradient id="redBlade" x1="0" y1="0" x2="1" y2="0">
      <stop offset="0" stop-color="#c4171d"/>
      <stop offset=".5" stop-color="#ee3338"/>
      <stop offset="1" stop-color="#e2272c"/>
    </linearGradient>
    <linearGradient id="redFold" x1="0" y1="0" x2="1" y2="0">
      <stop offset="0" stop-color="#5e0b0e"/>
      <stop offset="1" stop-color="#9b1419"/>
    </linearGradient>
    <linearGradient id="blueBlade" x1="0" y1="0" x2="1" y2="0">
      <stop offset="0" stop-color="#2a6d9b"/>
      <stop offset="1" stop-color="#0f3f66"/>
    </linearGradient>
  </defs>
  <rect x="0" y="180" width="35" height="330" fill="url(#redFold)"/>
  <polygon points="35,75 185,155 185,510 35,590" fill="url(#redBlade)"/>
  <polygon points="620,345 760,280 760,775 620,690" fill="url(#blueBlade)"/>
</svg>

<div class="abs academy-bg"></div>

<h1 class="abs title">Service Excellence</h1>

<div class="photo photo--workshop" role="img" aria-label="Photo of workshop participants gathered around a table outdoors"></div>
<div class="abs tagline">RIGOROUS TRAINING<br>FOR COMMUNITY<br>ORGANIZING</div>

<section class="abs partner">
  <h2>Partner with Us</h2>
  <h3>Your Subtitle Here</h3>
  <p>The Center looks to establish a permanent New York City infrastructure that will promote community organizing and leadership development, foster the identification, recruitment, and training of new organizers and leaders, and then offer career development support to the organizers and their respective organizations.</p>
  <p style="width:350px">Sandis aborpore alitem sitatiassed magni sdfdrv awfed autatem ulpa non nosa que accusanit vendiciet utem qua quia doluptatem exceped quaes quiae. Berovitae di dolorest dolupta quoditi busdae cullaut lis es sequat. Nam, torum, arum esto asdsa beatur, cus exces modis moluptis non consedipit. Ucia que pel est vendaest reniandit.Ga. Ditaten debitis citem. Ihit eaquamdsfevklu/</p>
</section>

<section class="abs results">
  <h2>Our Results</h2>
  <p>Atist, sanit, sandis aborpore alitem sitatiassed magni sdfdrv awfed autatem ulpa non nosa que accusanit vendiciet utem qua quia doluptatem exceped quaes quiae. Berovitae di dolorest dolupta quoditi busdae cullaut lis es sequat. Nam, torum, arum esto asdsa beatur, cus exces modis moluptis non consedipit. Ucia que pel est vendaest reniandit.Ga. Ditaten debitis citem. Ihit eaquamdsfevklu qui bla que eum dolorum isim et erro dolestiurepe pori officia.</p>
  <table class="data-table">
    <thead>
      <tr><th>ACTIVITY</th><th>PRETEST 2012</th><th>POSTTEST 2013</th><th>GROWTH</th></tr>
    </thead>
    <tbody>
      <tr><td>Graduation</td><td>123</td><td>321</td><td>161%</td></tr>
      <tr><td>Civic Engagement</td><td>123</td><td>321</td><td>161%</td></tr>
      <tr><td>Voter Registration</td><td>123</td><td>321</td><td>161%</td></tr>
      <tr><td>Jobs Placement</td><td>123</td><td>321</td><td>161%</td></tr>
      <tr><td>Leadership Training</td><td>123</td><td>321</td><td>161%</td></tr>
      <tr><td>Activity</td><td>123</td><td>321</td><td>161%</td></tr>
      <tr><td>Activity</td><td>123</td><td>321</td><td>161%</td></tr>
    </tbody>
  </table>
</section>

<section class="abs contact">
  <h2>Contact Us</h2>
  <div class="rule"></div>
  <p>Im estinciliqui bla cons di lorem irilisl dipsustio dunt dolore correvae cortin henim euip et aliquatummy nis nullaore faccum dolore et, sed tie volorper ing ex ent ea core eugiat.Abo. Itatium auditib usdandunt a aut.</p>
</section>
<div class="photo photo--group" role="img" aria-label="Aerial photo of a large group of program participants"></div>

<section class="abs program program--apprentice">
  <h2>Apprenticeship Program</h2>
  <p>Sandis aborpore alitem sitatiassed magni sdfdrv awfed autatem ulpa non nosa que accusanit vendiciet utem qua quia doluptatem exceped quaes aquaiae. Bferoavitae di dolosrest doluptsa qusod bausdae cullaut lis es swequaat. Nam, torum, arum Ucia que pel est vendaest raeniaqndit.Ga. Ditawten debitis citem. Ihit eaquamdsfevklua qui bla que euam dolorawum isims et eraqro dolestiurepe pori officia simus dipsaer sperro mivlop bernam que re ommo dolorenat cvgsk periasp ium et aped fgre que rerores tibusapiet dfwer ddefbryze porepelis debis dolut venimusam, repratus explam sit facullecum accuscilit volorrum quaerspis mo beaque.Met aliquatecaes ce aut velibusciet latem di.</p>
</section>

<section class="abs program program--academy">
  <h2>Organizing Academy</h2>
  <p>Sandis aborpore alitem sitatiassed magni sdfdrv awfed autatem ulpa non nosa que accusanit vendiciet utem qua quia doluptatem exceped quaes quiae. Berovitae di dolorest dolupta quoditi busdae cullaut lis es sequat. Nam, torum, arum esto asdsa beatur, cus exces modis moluptis non consedipit. Ucia que pel est vendaest reniandit.Ga. Ditaten debitis citem. Ihit dolorent cvgsk periasp ictur, expernatem efewconeces totatem ium deebis deolut venimseusam, repratus explam sit facullecum accuscilit volorrum quaerspis mo beaque.Met aliquatecaes ce aut velibusciet latem di.Caborrorrum excerro eum qui core</p>
</section>

<svg class="abs chart" width="340" height="230" viewBox="830 715 340 230" role="img" aria-label="Donut chart showing five factors adding to 100 percent">
  <g transform="rotate(-90 1010 822)" fill="none" stroke-width="26">
    <circle cx="1010" cy="822" r="65" pathLength="100" stroke="#c7e8f8" stroke-dasharray="8 92" stroke-dashoffset="0"/>
    <circle cx="1010" cy="822" r="65" pathLength="100" stroke="#a8dcf5" stroke-dasharray="25 75" stroke-dashoffset="-8"/>
    <circle cx="1010" cy="822" r="65" pathLength="100" stroke="#6ccaf1" stroke-dasharray="12 88" stroke-dashoffset="-33"/>
    <circle cx="1010" cy="822" r="65" pathLength="100" stroke="#1fb4ec" stroke-dasharray="25 75" stroke-dashoffset="-45"/>
    <circle cx="1010" cy="822" r="65" pathLength="100" stroke="#dff1fb" stroke-dasharray="30 70" stroke-dashoffset="-70"/>
  </g>
  <text class="chart-total" x="1010" y="834" text-anchor="middle">100<tspan>%</tspan></text>

  <g stroke="var(--chart-line)" stroke-width="1.2" fill="none">
    <polyline points="848,760 935,760 962,792"/>
    <polyline points="1140,741 1028,741 1013,768"/>
    <polyline points="1142,772 1058,772 1048,790"/>
    <polyline points="1142,897 1058,897 1042,866"/>
    <polyline points="848,900 935,900 966,868"/>
  </g>
  <text class="chart-label" x="851" y="752">Factor #1</text>
  <text class="chart-label" x="1030" y="733">Factor #2</text>
  <text class="chart-label" x="1058" y="767">Factor #3</text>
  <text class="chart-label" x="1058" y="891">Factor #4</text>
  <text class="chart-label" x="851" y="895">Factor #5</text>

  <g stroke="#4a7fa6" stroke-width=".8">
    <rect x="847" y="914" width="13" height="13" fill="#ffffff"/>
    <rect x="920" y="914" width="13" height="13" fill="#dff1fb"/>
    <rect x="993" y="914" width="13" height="13" fill="#a8dcf5"/>
    <rect x="1066" y="914" width="13" height="13" fill="#6ccaf1"/>
    <rect x="1136" y="914" width="13" height="13" fill="#1fb4ec"/>
  </g>
  <text class="legend-label" x="853" y="936" text-anchor="middle">Factor #1</text>
  <text class="legend-label" x="926" y="936" text-anchor="middle">Factor #2</text>
  <text class="legend-label" x="999" y="936" text-anchor="middle">Factor #3</text>
  <text class="legend-label" x="1072" y="936" text-anchor="middle">Factor #4</text>
  <text class="legend-label" x="1142" y="936" text-anchor="middle">Factor #5</text>
</svg>

</body>
</html>
```